QuietPerchHub.net No Ankle Bracelet required

We need Brief introduction to our product line! Could use pic of iPhone/Android smartphone next to Driftwise and a VrLok( our house arrest bracelet) Then list product line:
T-Node LoopGuard: No Ankle Bracelet required monitoring
T-Node VR-Lok: Wrist worn tamper proof wearable tethers smartphone
T-Node SOB: Alcohol Monitoring Program
T-Node t-bond: Paperless Bail Bond Program
Updates

i noticed most of our design entries appear to be different copy and paste versions of our website and of course the items I uploaded. We were hoping for more original designs? Only a few designs added content not already provided on website or upload. a little disappointed with process. Please advise if I did not post brief properly or simply did not understand this process of design?

Reason: Traveling last week and holiday weekend no time to review project.

Target Market(s)

Probation and Parole,Sheriffs,judges,bail agents, jails,prisons,immigration,

Industry/Entity Type

Legal

Font styles to use
Sans Serif

Colors
3176b5
ffffff

Requirements
Must have
• Description of entire product line
• pics
• tag line
• link to website
Nice to have
• video

```html
<!DOCTYPE html>
<html lang="en">
<head>
<meta charset="utf-8">
<title>T-Node House Arrest App</title>
<link href="https://fonts.googleapis.com/css2?family=Bitter:wght@600;700&family=Montserrat:wght@400;500;600&display=swap" rel="stylesheet">
<style>
:root{
  --navy:#2b3052;
  --ink:#1f2a52;
  --blue:#3176b5;
  --sky:#1a8cf0;
  --sky-light:#5db7ff;
  --link:#2e9bff;
  --white:#ffffff;
  --stage:#eef1f6;
  --muted:#4a4f66;
  --line:#c9ccd6;
}
*{margin:0;padding:0;box-sizing:border-box}
html,body{width:683px;height:1200px;overflow:hidden;background:var(--stage)}
body{font-family:"Montserrat",sans-serif;color:var(--ink);position:relative}
.page{position:absolute;left:164px;top:36px;width:356px;height:1128px;background:var(--white);border-radius:3px;overflow:hidden;box-shadow:0 2px 10px rgba(30,40,80,.12)}
.abs{position:absolute}
.slab{font-family:"Bitter",serif;font-weight:700}

/* header */
.brand-mark{left:0;width:356px;top:46px;text-align:center;font-family:"Montserrat",sans-serif;font-weight:600;font-size:13px;color:var(--ink)}
.brand-mark .dot{display:block;margin:0 auto 4px;width:26px;height:26px;border-radius:50%;background:var(--ink)}
.intro-box{left:35px;top:82px;width:285px;height:99px;border:1px solid var(--ink);text-align:center}
.intro-title{margin-top:26px;font-size:14.5px;line-height:16px;color:var(--ink)}
.intro-sub{margin-top:8px;font-size:6.6px;line-height:8.5px;color:var(--ink)}

/* video */
.video{left:0;top:206px;width:356px;height:200px;background:linear-gradient(180deg,#0c1733 0%,#16305e 100%)}
.video-site{left:6px;top:5px;font-size:6px;color:var(--white)}

/* features */
.feature-band{left:0;top:406px;width:356px;height:267px;background:radial-gradient(ellipse at 50% 85%,var(--sky-light) 0%,var(--sky) 70%)}
.feature-card{left:89px;top:425px;width:178px;height:301px;background:var(--white);border-radius:11px;overflow:hidden;box-shadow:0 1px 4px rgba(0,0,0,.1)}
.feature-head{height:55px;background:var(--navy);color:var(--white);text-align:center;padding-top:8px}
.feature-head h2{font-size:11.5px;line-height:13px}
.feature-head p{font-size:6.5px;margin-top:4px}
.feature-foot{position:absolute;left:0;bottom:0;width:178px;height:32px;background:var(--navy)}
.feature-icon{left:58px;top:79px}
.feature-name{left:0;width:178px;top:151px;text-align:center;font-size:11px;line-height:13px;color:var(--ink)}
.feature-desc{left:26px;width:126px;top:181px;text-align:center;font-size:5.2px;line-height:7.2px;color:var(--muted)}
.arrow{top:154px;font-size:9px;color:var(--ink)}

/* products */
.products-title{left:0;width:356px;top:759px;text-align:center;font-size:9px;color:var(--ink)}
.product-list{left:30px;top:783px;width:140px;list-style:none}
.product-list li{font-size:5px;line-height:7px;color:var(--muted)}
.product-list b{display:block;font-weight:600;color:var(--ink)}
.product-list li+li{margin-top:17px}
.product-list li.two+li{margin-top:11px}
.product-visual{left:180px;top:784px;width:160px;height:136px;border-radius:8px;background:linear-gradient(135deg,#f2f4f7 0%,#c9ced6 55%,#2a2c33 100%)}

/* newsletter */
.newsletter{left:0;top:940px;width:356px;height:98px;background:var(--navy);color:var(--white)}
.news-title{left:21px;top:27px;font-size:8.6px;line-height:11px}
.news-title a{color:var(--link);text-decoration:underline}
.news-text{left:21px;top:53px;font-size:6.6px;line-height:8.3px}
.news-input{left:188px;top:36px;width:112px;height:21px;background:var(--white);font-size:5px;color:#9aa0ae;padding:7px 5px;border-radius:2px 0 0 2px}
.news-btn{left:300px;top:36px;width:27px;height:21px;background:var(--link);font-size:5.3px;color:var(--white);text-align:center;line-height:21px;border-radius:0 2px 2px 0}

/* footer */
.foot-brand{left:38px;top:1050px;width:64px;text-align:center;font-size:7px;font-weight:600;color:var(--ink)}
.foot-brand .dot{display:block;margin:0 auto 2px;width:14px;height:14px;border-radius:50%;background:var(--ink)}
.copyright{left:36px;top:1082px;width:68px;text-align:center;font-size:4.7px;line-height:6.5px;color:var(--muted)}
.dl-title{left:110px;top:1049px;font-size:6.3px;font-weight:600;color:var(--ink)}
.dl-col{top:1060px;font-size:4.8px;line-height:6.3px;color:var(--muted)}
.store-btn{top:1081px;height:17px;border:1px solid var(--line);border-radius:2px;font-size:5.2px;line-height:15px;text-align:center;color:var(--ink);background:var(--white)}
.footnote{left:113px;top:1104px;font-size:4.6px;color:var(--muted)}
</style>
</head>
<body>
<main class="page">

  <header>
    <div class="abs brand-mark"><span class="dot"></span>T-Node</div>
    <div class="abs intro-box">
      <h1 class="slab intro-title">Introducing the T-Node HOUSE<br>ARREST APP</h1>
      <p class="intro-sub">More Effective &amp; Complete Electronic Monitoring--<br><i>without</i> Ankle Bracelets!</p>
    </div>
  </header>

  <section class="abs video" role="img" aria-label="Explainer video still: the offender's wristband and smartphone send location through the cloud to a monitoring agency tablet map">
    <span class="abs video-site">QuietPerchHub.net</span>
  </section>

  <section class="abs feature-band"></section>
  <article class="abs feature-card">
    <div class="feature-head">
      <h2 class="slab">Advanced Electronic<br>Monitoring</h2>
      <p>The T-Node Advantage:</p>
    </div>
    <svg class="abs feature-icon" width="62" height="62" viewBox="0 0 62 62" aria-hidden="true">
      <circle cx="31" cy="31" r="29.5" fill="none" stroke="var(--ink)" stroke-width="2"/>
      <g transform="rotate(45 33 27)" fill="var(--ink)">
        <rect x="29" y="21" width="8" height="12" rx="2"/>
        <rect x="20" y="24" width="7" height="6"/>
        <rect x="39" y="24" width="7" height="6"/>
      </g>
      <path d="M17 37 a10 10 0 0 0 8 8" fill="none" stroke="var(--ink)" stroke-width="2"/>
      <path d="M13 38 a15 15 0 0 0 11 11" fill="none" stroke="var(--ink)" stroke-width="2"/>
    </svg>
    <span class="abs arrow" style="left:5px">&#8249;</span>
    <span class="abs arrow" style="right:5px">&#8250;</span>
    <h3 class="abs slab feature-name">Real-time GPS<br>Tracking</h3>
    <p class="abs feature-desc">Enrollee movements are monitored and tracked via Global Positioning System (GPS) technology. Violation alerts can be set with geo-fencing parameters.</p>
    <div class="feature-foot"></div>
  </article>

  <section>
    <h2 class="abs slab products-title">Our T-Node Product line includes:</h2>
    <ul class="abs product-list">
      <li><b>T-Node LoopGuard:</b>No Ankle Bracelet required monitoring</li>
      <li class="two"><b>T-Node VR-Lok:</b>Wrist worn tamper proof wearable that tethers your smartphone</li>
      <li><b>T-Node SOB:</b>Alcohol Monitoring Program</li>
      <li><b>T-Node t-bond:</b>Paperless Bail Bond Program</li>
    </ul>
    <div class="abs product-visual" role="img" aria-label="Product photo: smartphone showing the check-in screen beside a black wrist band and a handheld breath alcohol tester"></div>
  </section>

  <section class="abs newsletter">
    <p class="abs slab news-title">For the latest news on the T-Node<br>House Arrest App, sign up <a>here</a>:</p>
    <p class="abs news-text">You'll be among the first to know about<br>important news and upcoming features.</p>
    <div class="abs news-input">Enter your email address</div>
    <div class="abs news-btn">Sign up</div>
  </section>

  <footer>
    <div class="abs foot-brand"><span class="dot"></span>T-Node</div>
    <p class="abs copyright">© 2015 QuietPerch Hub,<br>LLC. All rights reserved.</p>
    <p class="abs dl-title">Available Now for Download on the AppDepot* &amp; PlayMart*:</p>
    <p class="abs dl-col" style="left:110px">T-Node HOUSE ARREST ADMIN APP<br>(for Monitoring Agencies)</p>
    <p class="abs dl-col" style="left:214px">T-Node HOUSE ARREST APP<br>(for Enrollees)</p>
    <div class="abs store-btn" style="left:112px;width:47px">AppDepot</div>
    <div class="abs store-btn" style="left:215px;width:47px">AppDepot</div>
    <div class="abs store-btn" style="left:266px;width:47px">PlayMart</div>
    <p class="abs footnote">*Sign-up Required before Activation</p>
  </footer>

</main>
</body>
</html>
```